Boracay Wedding Invitation Design

Hello, We would like a wedding invitation design for our wedding in Boracay. We would like it somewhat in the form of a boarding pass with beachy fresh colours, possibly a nice Boracay beach in the background Double sided with an envelope design to match. Maybe something simple on the envelope like a nice picture in the bottom left corner of a shell on a beach or something similar.

I would also like on the opposite side of the invite to be an "information sheet" with a matching beach design

The text files for both sides are included and i have also included 2 designs that i thought looked nice and are similar to what we are after.
Updates

Hello, I have updated the brief to be more specific with text files and images to make it easier for you. Thank you :)

Industry/Entity Type

Wedding

Font styles to use
Decorative
Script

Colors
fbee3d
33a6d7
33b8a4
fbf289
85cae6
ffffff

Requirements
Must have
• I would like to have this quote somewhere on the invitation
• This day I will marry my best friend,
• the one I laugh with,
• live for,
• dream with,
• love
• Owen & Marisa
• Request the pleasure of your company to celebrate their wedding
• On Friday the 17th March 2017
• at
• Velunda Grand Suites
• Boracay, Philippines
• Ceremony begins at 3.00pm
• RSVP
• Owen 0431907254
• Marisa 0417283649
• by
• 17th Jan 2016
• Dress: Beach Formal
• For the "information sheet"
• There will be a 5% discount on rooms booked at the Velunda under the event Owen & Marisa Wedding. The resort has a total of 24 rooms it would be nice if the majority of guests could stay at the resort from the night before until the night after the wedding but if you choose to stay elsewhere on the island there are plenty of other places to stay for cheaper and everything is fairly close as its a small island.
• We have currently blocked room stay for a short period of time so our guests can book rooms. If you choose to do so please email reservations@velundastays.example. Once rooms become available to the public again, towards the end of Jan, it will be first come first served basis. The resort is very popular so im assuming once this happens the rooms will be booked out.
• If you would like to check out the resort itself the website is www.velundagrand-isle.example
• We know its a fair distance to travel but we would really love to see you all there to celebrate and maybe even enjoy a small holiday while your here its a beautiful part of the world.
• If anyone has any questions please feel free to contact Owen on 0431907254
Nice to have
• A nice picture of a Boracay beach in the background would be nice

```html
<!DOCTYPE html>
<html lang="en">
<head>
<meta charset="utf-8">
<title>Owen &amp; Marisa – Boracay Wedding Invitation</title>
<link rel="stylesheet" href="https://fonts.googleapis.com/css2?family=Great+Vibes&family=Quicksand:wght@500;600;700&display=swap">
<style>
  :root {
    --sky: #8ccbea;
    --lemon: #f7f28a;
    --envelope: #f4f0a4;
    --cocoa: #4a2c18;
    --sea: #33b8a4;
    --ocean: #33a6d7;
    --sand: #f5b04a;
    --white: #ffffff;
    --script: "Great Vibes", cursive;
    --sans: "Quicksand", sans-serif;
  }
  * { box-sizing: border-box; margin: 0; padding: 0; }
  html, body { width: 1200px; height: 800px; overflow: hidden; background: var(--white); }
  body { position: relative; font-family: var(--sans); color: var(--cocoa); }

  .ticket {
    position: absolute;
    width: 690px; height: 340px;
    background: var(--sky);
    border-radius: 10px;
    padding: 12px;
    display: flex; gap: 5px;
  }
  .ticket--front { left: 40px; top: 40px; }
  .ticket--back { left: 470px; top: 420px; }

  .stub {
    background: var(--lemon);
    border-radius: 8px;
    display: flex; flex-direction: column; align-items: center; justify-content: space-between;
    padding: 14px 0;
  }
  .stub--side { width: 58px; }
  .stub--side.is-left { border-right: 1.5px dashed var(--cocoa); }
  .stub--side.is-right { border-left: 1.5px dashed var(--cocoa); }

  .flower {
    width: 30px; height: 30px; border-radius: 50%;
    background: var(--cocoa);
  }
  .plane { width: 30px; height: 30px; fill: var(--cocoa); }

  .stub__label {
    writing-mode: vertical-rl; transform: rotate(180deg);
    display: flex; align-items: center; gap: 2px;
  }
  .stub__names { font-family: var(--script); font-size: 26px; line-height: 1; }
  .stub__tag { font-size: 9px; font-weight: 700; letter-spacing: .5px; text-transform: uppercase; }

  .hero {
    flex: 1; position: relative; border-radius: 8px; overflow: hidden;
    padding: 18px 24px 14px;
    text-align: center;
  }
  .hero__scene {
    position: absolute; inset: 0;
    background: linear-gradient(180deg, #dcefff 0%, #a9dcf3 28%, #5fc6d6 45%, #3fb6c0 55%, #f7e9a6 68%, #f7c36a 82%, #f2a83c 100%);
  }
  .hero__content { position: relative; }
  .quote { font-size: 11.5px; font-weight: 700; text-transform: uppercase; line-height: 1.55; }
  .couple { font-family: var(--script); font-size: 62px; line-height: 1; margin: 4px 0 2px; font-weight: 400; }
  .request { font-size: 12px; font-weight: 700; text-transform: uppercase; line-height: 1.3; }
  .details {
    display: grid; grid-template-columns: 1fr 1fr; column-gap: 20px; row-gap: 8px;
    text-align: left; margin-top: 20px; padding: 0 6px;
  }
  .details dt { font-size: 9px; font-weight: 600; text-transform: uppercase; }
  .details dd { font-size: 11.5px; font-weight: 700; }

  .stub--rsvp {
    width: 132px; border-left: 1.5px dashed var(--cocoa);
    justify-content: flex-start; text-align: center; padding: 16px 6px;
  }
  .rsvp__title { font-size: 13px; font-weight: 700; margin-bottom: 12px; }
  .rsvp__lines { font-size: 10.5px; font-weight: 700; line-height: 1.35; }
  .datebox {
    margin: 22px 0 26px;
    width: 86px; height: 86px; border-radius: 8px;
    background: var(--cocoa); color: var(--lemon);
    display: flex; flex-direction: column; align-items: center; justify-content: center;
  }
  .datebox__month { font-size: 13px; font-weight: 700; }
  .datebox__day { font-size: 44px; font-weight: 700; line-height: 1; }
  .dress dt { font-size: 10px; font-weight: 700; text-transform: uppercase; }
  .dress dd { font-size: 10.5px; font-weight: 700; }

  .info {
    flex: 1; background: var(--lemon); border-radius: 8px;
    display: grid; grid-template-columns: 1fr 1fr; column-gap: 22px;
    padding: 16px 20px;
  }
  .info__col { display: flex; flex-direction: column; gap: 10px; }
  .info p { font-size: 10.6px; font-weight: 600; line-height: 1.35; }
  .info strong { font-weight: 700; }
  .info__rule { width: 40px; border-top: 1.5px dashed var(--cocoa); }
  .info .info__note { font-size: 9.5px; }
  .stub--side .stub__date { font-size: 9px; font-weight: 700; letter-spacing: .4px; text-transform: uppercase; }

  .envelope {
    position: absolute; left: 40px; top: 420px;
    width: 400px; height: 340px;
    background: var(--envelope);
    border-radius: 2px;
  }
  .envelope__mark {
    position: absolute; right: 34px; bottom: 30px;
    display: flex; align-items: center; gap: 8px;
  }
  .envelope__mark .flower { width: 44px; height: 44px; }
  .envelope__names { font-family: var(--script); font-size: 50px; line-height: .85; text-align: center; }
</style>
</head>
<body>

<section class="ticket ticket--front" aria-label="Invitation front">
  <div class="stub stub--side is-left">
    <div class="flower" role="img" aria-label="Hibiscus flower emblem"></div>
    <div class="stub__label">
      <span class="stub__names">Owen &amp; Marisa</span>
      <span class="stub__tag">Boarding Pass</span>
    </div>
    <svg class="plane" viewBox="0 0 24 24" aria-hidden="true"><path d="M2 10.8h7.5L13.6 3h2.2l-2.4 7.8h5.4l2-2.3h1.4l-1 3.5 1 3.5h-1.4l-2-2.3h-5.4l2.4 7.8h-2.2l-4.1-7.8H2z"/></svg>
  </div>

  <div class="hero">
    <div class="hero__scene" role="img" aria-label="Tropical beach with palm fronds, turquoise sea and golden sand"></div>
    <div class="hero__content">
      <p class="quote">This day I will marry my best friend,<br>the one I laugh with,<br>live for,<br>dream with,<br>love</p>
      <h1 class="couple">Owen &amp; Marisa</h1>
      <p class="request">Request the pleasure of your company to<br>celebrate their wedding</p>
      <dl class="details">
        <div><dt>Date:</dt><dd>On Friday the 17th March 2017</dd></div>
        <div><dt>Location:</dt><dd>Boracay, Philippines</dd></div>
        <div><dt>Destination:</dt><dd>at Velunda Grand Suites</dd></div>
        <div><dt>Time:</dt><dd>Ceremony begins at 3.00pm</dd></div>
      </dl>
    </div>
  </div>

  <div class="stub stub--rsvp">
    <p class="rsvp__title">RSVP</p>
    <p class="rsvp__lines">Owen 0431907254<br>Marisa 0417283649<br>by 17th Jan 2016</p>
    <div class="datebox">
      <span class="datebox__month">MAR 2017</span>
      <span class="datebox__day">17</span>
    </div>
    <dl class="dress"><dt>Dress:</dt><dd>Beach Formal</dd></dl>
  </div>
</section>

<section class="envelope" aria-label="Envelope">
  <div class="envelope__mark">
    <div class="flower" role="img" aria-label="Hibiscus flower emblem"></div>
    <p class="envelope__names">Owen<br>&amp;<br>Marisa</p>
  </div>
</section>

<section class="ticket ticket--back" aria-label="Information sheet">
  <div class="info">
    <div class="info__col">
      <p>There will be a 5% discount on rooms booked at the Velunda under the event Owen &amp; Marisa Wedding. The resort has a total of 24 rooms it would be nice if the majority of guests could stay at the resort from the night before until the night after the wedding but if you choose to stay elsewhere on the island there are plenty of other places to stay for cheaper and everything is fairly close as its a small island.</p>
      <p>We have currently blocked room stay for a short period of time so our guests can book rooms. If you choose to do so please email <strong>reservations@velundastays.example</strong>. Once rooms become available to the public again, towards the end of Jan, it will be first come first served basis.</p>
    </div>
    <div class="info__col">
      <p>The resort is very popular so I'm assuming once this happens the rooms will be booked out.</p>
      <p>If you would like to check out the resort itself the website is <strong>www.velundagrand-isle.example</strong></p>
      <p>We know its a fair distance to travel but we would really love to see you all there to celebrate and maybe even enjoy a small holiday while your here its a beautiful part of the world.</p>
      <div class="info__rule"></div>
      <p class="info__note">If anyone has any questions please feel free to contact Owen on 0431907254</p>
    </div>
  </div>
  <div class="stub stub--side is-right">
    <div class="flower" role="img" aria-label="Hibiscus flower emblem"></div>
    <div class="stub__label">
      <span class="stub__names">Owen &amp; Marisa</span>
      <span class="stub__date">Friday the 17th March 2017</span>
    </div>
    <svg class="plane" viewBox="0 0 24 24" aria-hidden="true"><path d="M2 10.8h7.5L13.6 3h2.2l-2.4 7.8h5.4l2-2.3h1.4l-1 3.5 1 3.5h-1.4l-2-2.3h-5.4l2.4 7.8h-2.2l-4.1-7.8H2z"/></svg>
  </div>
</section>

</body>
</html>
```